Stationary Design for Medical Distribution Company

We are a Medical Distribution Company based in Dar es salaam, Tanzania (East Africa). Our company was established in 1995 and we are a reputed and respected Pharmaceuticals and Medical Supplies company in the region.
We have just recently changed our company logo. A new company logo has just recently been selected through Pixel Harbor and we are now looking for stationary designs such as Business Cards, Letterheads, Envelopes, etc.. for our company.
We request you all to take a look at the attached new company logo and give us your best possible designs.
We would prefer to have a double sided business card. For letterheads, we are open to your ideas/designs.
We are looking forward for your designs!
Updates
Company details to be incorporated in designs:
Company Name: KOVEL PHARMACEUTICALS LIMITED
Company Address: Office # 42, Tumaini Works Ltd., Msasani Lane, Dar es salaam, Tanzania
Tel: +255 22 2917348 / 49, Fax: +255 22 2917350
Email: info@kovelmedix.example
Website: www.kovelmedix.example
Also should include Cell number +255 XXX XXX XXX
Name and Designation.....
Target Market(s)
Medical Sector
Industry/Entity Type
Medical
Look and feel

```html
<!DOCTYPE html>
<html lang="en">
<head>
<meta charset="utf-8">
<title>Kovel Pharmaceuticals – Business Card</title>
<link rel="stylesheet" href="https://fonts.googleapis.com/css2?family=Encode+Sans+Condensed:wght@800&display=swap">
<style>
  :root {
    --brand-red: #c43c3d;
    --ink: #111111;
    --paper: #ffffff;
    --wash: #f6dcdc;
  }
  html, body {
    margin: 0;
    padding: 0;
    overflow: hidden;
    background: var(--paper);
  }
  .card {
    position: relative;
    width: 1200px;
    height: 686px;
    overflow: hidden;
    background: var(--paper);
    font-family: "Encode Sans Condensed", "Arial Narrow", sans-serif;
    font-weight: 800;
    color: var(--ink);
  }
  .brand-wash {
    position: absolute;
    left: 300px;
    top: 30px;
    width: 800px;
    height: 620px;
    background: radial-gradient(ellipse at center, var(--wash) 0%, rgba(246,220,220,0.35) 45%, rgba(255,255,255,0) 72%);
  }
  .brand-mark {
    position: absolute;
    left: 66px;
    top: 63px;
    width: 260px;
    height: 263px;
    border-radius: 24px;
    background: var(--brand-red);
    display: flex;
    align-items: center;
    justify-content: center;
  }
  .brand-name {
    color: var(--paper);
    font-size: 58px;
    letter-spacing: 2px;
  }
  .holder {
    position: absolute;
    left: 357px;
    top: 94px;
    margin: 0;
    font-size: 52px;
    line-height: 68px;
  }
  .holder-name, .holder-role {
    display: block;
  }
  .contact, .address {
    position: absolute;
    top: 377px;
    margin: 0;
    padding: 0;
    list-style: none;
    font-size: 37px;
    line-height: 51.5px;
    white-space: nowrap;
  }
  .contact {
    right: 472px;
    text-align: right;
  }
  .address {
    left: 797px;
    font-style: normal;
  }
</style>
</head>
<body>
  <main class="card">
    <div class="brand-wash" role="img" aria-label="Faint pale red brand decoration behind the card text"></div>

    <div class="brand-mark">
      <span class="brand-name">KOVEL</span>
    </div>

    <h1 class="holder">
      <span class="holder-name">Daniel Mwakalinga</span>
      <span class="holder-role">Manager in Charge of Accounts</span>
    </h1>

    <ul class="contact">
      <li>Tel: +255 22 2917348 / 49</li>
      <li>Fax: +255 22 2917350</li>
      <li>Email: info@kovelmedix.example</li>
      <li>Website: www.kovelmedix.example</li>
      <li>Cell: +255 XX XXXXXXX</li>
    </ul>

    <address class="address">
      Office #42<br>
      Tumaini Works Ltd.<br>
      Msasani Lane<br>
      Dar es salaam<br>
      Tanzania
    </address>
  </main>
</body>
</html>
```